KD Group Company brochure

require the design of a brochure for my company KD group which incorporates 2 separate companies specialising in home technology and security. Im not sure whether its going to be best to do one brochure with all the info in or 2 individual ones

Target Market(s)

Footballers and High net worth individuals

Industry/Entity Type

Information Technology

Font styles to use
Serif
Other font styles liked:
• Neuropol (this is the logo font)

Colors
ec1f27
000000
9d9d9d

Requirements
Must have
• 2 sections one for audio visual and 1 for security

```html
<!DOCTYPE html>
<html lang="en">
<head>
<meta charset="utf-8">
<title>KD Group Brochure</title>
<link href="https://fonts.googleapis.com/css2?family=Open+Sans:wght@400;600;700&display=swap" rel="stylesheet">
<style>
:root{
  --red:#ec1f27;
  --red-dark:#8e0f14;
  --black:#000000;
  --grey:#9d9d9d;
  --white:#ffffff;
  --stage:#dcdcdc;
  --navy:#10131f;
}
*{margin:0;padding:0;box-sizing:border-box}
html,body{width:800px;height:1200px;overflow:hidden;background:var(--stage);font-family:"Open Sans",sans-serif;color:var(--white)}
.spread{position:absolute;left:20px;width:760px;height:537px;background:var(--black);overflow:hidden;box-shadow:0 4px 14px rgba(0,0,0,.35)}
.cover{top:20px}
.inside{top:620px}
.spread>svg{position:absolute;left:0;top:0}
.fold{position:absolute;left:379px;top:0;width:2px;height:100%;background:rgba(255,255,255,.06)}
.abs{position:absolute}
.about{left:228px;top:36px;width:142px}
.about h2{font-size:11px;font-weight:600;margin-bottom:6px}
.about p{font-size:7.5px;line-height:1.45}
.contact{font-size:8.5px;line-height:1.4}
.address{left:30px;top:462px;display:flex;gap:6px}
.phone{left:160px;top:490px;display:flex;gap:5px;align-items:center}
.email{left:262px;top:470px;display:flex;gap:5px;align-items:center}
.web{display:flex;gap:5px;align-items:center;font-size:9px}
.web-cover{left:455px;top:478px}
.web-inside{left:600px;top:506px}
.brand{left:600px;top:410px;display:flex;gap:7px;align-items:center}
.brand-mark{width:14px;height:14px;border-radius:50%;background:var(--red)}
.brand-name{font-size:14px;font-weight:700;color:var(--white)}
.column{font-size:6.6px;line-height:1.42;color:#e6e6e6}
.column p{margin-bottom:5px}
.column strong{color:var(--white)}
.col-left{left:22px;top:18px;width:330px}
.col-right{left:405px;top:18px;width:335px}
.section-title{display:inline-block;font-size:11px;font-weight:600;color:var(--red);padding:1px 30px 2px 6px;border-bottom:1px solid var(--red);border-left:1px solid var(--red);margin:4px 0 6px}
.ticks{list-style:none;margin-bottom:5px}
.ticks li{padding-left:10px;position:relative;margin-bottom:2px}
.ticks li::before{content:"✓";position:absolute;left:0;color:var(--red);font-weight:700}
</style>
</head>
<body>

<section class="spread cover">
  <svg width="760" height="537" viewBox="0 0 760 537">
    <defs>
      <linearGradient id="roomBrown" x1="0" y1="0" x2="1" y2="1">
        <stop offset="0" stop-color="#2a1a12"/>
        <stop offset=".5" stop-color="#4a3225"/>
        <stop offset="1" stop-color="#1a1210"/>
      </linearGradient>
      <linearGradient id="panelRed" x1="0" y1="0" x2="0" y2="1">
        <stop offset="0" stop-color="#ec1f27"/>
        <stop offset="1" stop-color="#8e0f14"/>
      </linearGradient>
      <linearGradient id="cinema" x1="0" y1="0" x2="0" y2="1">
        <stop offset="0" stop-color="#d9cfc4"/>
        <stop offset=".35" stop-color="#7a3e52"/>
        <stop offset="1" stop-color="#5b2a6e"/>
      </linearGradient>
      <clipPath id="aboveCurve"><path d="M0,0 H760 V300 Q300,480 0,430 Z"/></clipPath>
    </defs>
    <g clip-path="url(#aboveCurve)">
      <rect x="0" y="0" width="215" height="537" fill="url(#roomBrown)" role="img" aria-label="Photo of a media room with a wall-mounted control screen"/>
      <rect x="215" y="0" width="165" height="537" fill="url(#panelRed)"/>
      <rect x="380" y="0" width="380" height="537" fill="url(#cinema)" role="img" aria-label="Photo of a private home cinema with a large screen and purple carpet"/>
    </g>
    <path d="M0,430 Q300,480 760,300" fill="none" stroke="var(--red)" stroke-width="12"/>
    <path d="M0,442 Q300,492 760,312" fill="none" stroke="#d5d5d5" stroke-width="3"/>
    <rect x="240" y="300" width="118" height="72" rx="6" fill="var(--white)"/>
    <rect x="248" y="308" width="102" height="56" rx="3" fill="var(--red)"/>
  </svg>
  <div class="fold"></div>

  <div class="abs about">
    <h2>About us</h2>
    <p>With offices in London and Newcastle, we design, install and service entertainment and control systems for our clients. The service is personal, unintimidating and of the highest quality. We create systems that enrich and support our clients' lives, giving them the technology they need without the compromise.</p>
  </div>

  <div class="abs contact address">
    <svg width="8" height="11" viewBox="0 0 8 11"><path d="M4,0 A4,4 0 0 1 8,4 C8,7 4,11 4,11 C4,11 0,7 0,4 A4,4 0 0 1 4,0 Z" fill="var(--red)"/><circle cx="4" cy="4" r="1.5" fill="var(--black)"/></svg>
    <div>KD Group Ltd<br>Harwell House<br>118-120 Elmfield Road<br>London<br>SE9 4QT</div>
  </div>
  <div class="abs contact phone">
    <svg width="9" height="9" viewBox="0 0 10 10"><circle cx="5" cy="5" r="4.3" fill="none" stroke="var(--red)" stroke-width="1.2"/><path d="M3.4,3 L4.3,3 L4.6,4.3 L4.1,4.7 Q4.6,5.6 5.4,6 L5.8,5.5 L7,5.8 L7,6.7 Q4,7 3.4,3 Z" fill="var(--red)"/></svg>
    <span>0207 555 0182</span>
  </div>
  <div class="abs contact email">
    <svg width="10" height="7" viewBox="0 0 10 7"><rect x=".5" y=".5" width="9" height="6" fill="none" stroke="var(--red)"/><path d="M.5,.5 L5,4 L9.5,.5" fill="none" stroke="var(--red)"/></svg>
    <span>info@kdgroup-tech.co.uk</span>
  </div>

  <div class="abs brand">
    <span class="brand-mark"></span>
    <span class="brand-name">KD Group</span>
  </div>
  <div class="abs web web-cover">
    <svg width="9" height="9" viewBox="0 0 10 10"><circle cx="5" cy="5" r="4.3" fill="none" stroke="var(--red)" stroke-width="1.2"/><path d="M.7,5 H9.3 M5,.7 V9.3" stroke="var(--red)" stroke-width=".9"/></svg>
    <span>www.kdgroup-tech.co.uk</span>
  </div>
</section>

<section class="spread inside">
  <svg width="760" height="537" viewBox="0 0 760 537">
    <defs>
      <linearGradient id="night" x1="0" y1="0" x2="1" y2="1">
        <stop offset="0" stop-color="#05060a"/>
        <stop offset=".5" stop-color="var(--navy)"/>
        <stop offset="1" stop-color="#05060a"/>
      </linearGradient>
      <linearGradient id="thumb" x1="0" y1="0" x2="1" y2="1">
        <stop offset="0" stop-color="#6f7a94"/>
        <stop offset="1" stop-color="#2a3044"/>
      </linearGradient>
    </defs>
    <rect width="760" height="537" fill="url(#night)"/>
    <path d="M0,350 C150,430 300,470 420,468 L760,468 V537 H0 Z" fill="var(--black)"/>
    <path d="M0,350 C150,430 300,470 420,468 L760,468" fill="none" stroke="var(--red)" stroke-width="9"/>
    <path d="M0,361 C150,441 300,481 420,479 L760,479" fill="none" stroke="#d5d5d5" stroke-width="3"/>
    <g stroke="var(--red)" stroke-width="4" fill="url(#thumb)">
      <circle cx="60" cy="385" r="28" role="img" aria-label="Photo of a remote control and tablet"/>
      <circle cx="145" cy="422" r="26" role="img" aria-label="Photo of a home cinema room"/>
      <circle cx="235" cy="449" r="24" role="img" aria-label="Photo of a smart thermostat"/>
      <circle cx="430" cy="468" r="26" role="img" aria-label="Photo of an access control keypad"/>
      <circle cx="525" cy="468" r="30" role="img" aria-label="Photo of a secured building interior"/>
      <circle cx="650" cy="466" r="38" role="img" aria-label="Photo of a phone showing a door entry call"/>
    </g>
  </svg>
  <div class="fold"></div>

  <div class="abs column col-left">
    <h3 class="section-title">Audio Visual</h3>
    <p><strong>KD Group</strong> provides an extensive range of audio visual services, combining design, installation and support to give a complete end to end service.</p>
    <p>Our trained staff take a focused approach to the design and installation of control, lighting and cinema systems, delivering a complete and professional result.</p>
    <p>Our services include video conferencing, distributed audio, home cinema and digital signage, all managed from one simple interface that works anywhere in the home or office.</p>
    <p>Our designs combine a simple approach with a clear understanding of each client's needs, giving maximum user experience and lasting value.</p>
    <h3 class="section-title">Networks</h3>
    <p>It has always been our belief that whatever technology runs a business, it relies on the network it sits on.</p>
    <p><strong>KD Group</strong> is dedicated to providing customers with the right network platforms, designed to meet the requirements of today and the applications of tomorrow.</p>
    <p>Our solutions include design, installation and support of local area networks, wireless coverage and structured cabling for homes, offices and estates.</p>
  </div>

  <div class="abs column col-right">
    <h3 class="section-title">Unified Communications</h3>
    <p>Simplify business processes that depend on human interaction. Unified communications help close the gap between people, places and devices.</p>
    <p>By using the intelligence of the network, employees, partners and customers can connect in real time with greater speed and agility.</p>
    <ul class="ticks">
      <li>Collaborate across teams and work spaces with ease.</li>
      <li>Accelerate decision making with shared information.</li>
      <li>Innovate across the value chain with one platform.</li>
      <li>Integrate applications with the tools you use daily.</li>
    </ul>
    <h3 class="section-title">Building Security</h3>
    <p>At <strong>KD Group</strong> we look after your building with high quality security and access solutions, from CCTV and intruder alarms to door entry.</p>
    <p>With our combined expertise we integrate with existing or new infrastructure, so your building is protected and easy to manage.</p>
    <p>From single devices to complete integrated systems, each project is unique to you and your building.</p>
  </div>

  <div class="abs web web-inside">
    <svg width="9" height="9" viewBox="0 0 10 10"><circle cx="5" cy="5" r="4.3" fill="none" stroke="var(--red)" stroke-width="1.2"/><path d="M.7,5 H9.3 M5,.7 V9.3" stroke="var(--red)" stroke-width=".9"/></svg>
    <span>www.kdgroup-tech.co.uk</span>
  </div>
</section>

</body>
</html>
```